Marcus Pellow Carpentry & Joinery

Hello, I would like a flyer designed for my new business doing small projects in my local area for home-owners. I am a professional tradesman.
The type of work I am offering is:
- decks/decking
- external stairs & railings
- install windows & doors
- roofs & gutters
- small additions
- built-in wardrobes
- finish work
- demolition

It would be great if the flyer could mention these, or use phrasing that fits this kind of construction work.
My idea for a slogan was "new work and repairs to any age home".

Please also mention FREE QUOTES and have my email and phone number included on the flyer, along with my carpentry licence number, which I can provided.

I'd like a one page, single-sided flyer that could be printed as DL.
Colour and style is up to you! I'll be placing this flyer on counters & in the windows of local businesses, so something simple and eye-catching is preferred.

Thank you!

```html
<!DOCTYPE html>
<html lang="en">
<head>
<meta charset="utf-8">
<title>Marcus Pellow Carpentry &amp; Joinery – DL Flyer</title>
<link href="https://fonts.googleapis.com/css2?family=Alfa+Slab+One&family=Montserrat:wght@500;700&family=Varela+Round&display=swap" rel="stylesheet">
<style>
  :root {
    --backdrop: #d9d9d9;
    --navy: #0f1f5c;
    --royal: #1f3f9a;
    --sky: #3f6fc4;
    --yellow: #f5d216;
    --white: #ffffff;
    --sheet-top: #2a54b8;
    --sheet-bottom: #16307e;
    --lawn: #3f9a2e;
    --lawn-light: #6cc24a;
    --brick: #b98e6c;
  }
  * { box-sizing: border-box; margin: 0; padding: 0; }
  html, body { width: 1200px; height: 786px; overflow: hidden; }
  body {
    background: var(--backdrop);
    display: flex;
    align-items: center;
    justify-content: center;
  }
  .flyer {
    position: relative;
    width: 356px;
    height: 750px;
    overflow: hidden;
    background: linear-gradient(180deg, var(--navy) 0%, var(--royal) 30%, var(--sky) 48%);
    box-shadow: 0 10px 30px rgba(0,0,0,.35);
  }
  .brand {
    position: absolute;
    top: 40px; left: 0; right: 0;
    display: flex;
    align-items: center;
    justify-content: center;
    gap: 12px;
  }
  .brand-mark {
    width: 26px; height: 26px;
    background: var(--yellow);
    flex: none;
  }
  .brand-name {
    font-family: "Alfa Slab One", serif;
    font-weight: 400;
    color: var(--yellow);
    font-size: 23px;
    line-height: 1.15;
    text-align: left;
  }
  .offer {
    position: absolute;
    top: 122px; left: 50%;
    transform: translateX(-50%);
    padding: 4px 16px;
    border: 2px solid var(--yellow);
    font-family: "Montserrat", sans-serif;
    font-weight: 700;
    color: var(--white);
    font-size: 14px;
    letter-spacing: 2px;
    white-space: nowrap;
  }
  .headline {
    position: absolute;
    top: 168px; left: 0; right: 0;
    text-align: center;
    font-family: "Alfa Slab One", serif;
    font-weight: 400;
    color: var(--yellow);
    font-size: 19px;
    line-height: 1.15;
    letter-spacing: .3px;
  }
  .contact {
    position: absolute;
    top: 222px; left: 0; right: 0;
    text-align: center;
    font-family: "Montserrat", sans-serif;
    font-weight: 500;
    color: var(--white);
    font-size: 10px;
    line-height: 1.45;
    letter-spacing: .6px;
    text-transform: uppercase;
  }
  .scene {
    position: absolute;
    top: 285px; left: 0; right: 0; bottom: 0;
    background: linear-gradient(180deg,
      var(--sky) 0%, #7f9fd0 18%, var(--brick) 30%, #caa886 52%,
      var(--lawn-light) 62%, var(--lawn) 100%);
  }
  .services {
    position: absolute;
    top: 420px; left: -14px;
    width: 270px; height: 250px;
    padding: 22px 16px 0 30px;
    background: linear-gradient(160deg, var(--sheet-top), var(--sheet-bottom));
    transform: rotate(-7deg);
    transform-origin: top left;
    box-shadow: 0 4px 10px rgba(0,0,0,.3);
    list-style: none;
    font-family: "Varela Round", sans-serif;
    color: var(--white);
    font-size: 17px;
    line-height: 1.25;
  }
  .services li::before { content: "- "; }
</style>
</head>
<body>
  <main class="flyer">
    <div class="brand">
      <span class="brand-mark"></span>
      <span class="brand-name">Marcus Pellow<br>Carpentry &amp; Joinery</span>
    </div>

    <p class="offer">FREE QUOTES</p>

    <h1 class="headline">NEW WORK AND REPAIRS<br>TO ANY AGE HOME</h1>

    <div class="contact">
      <p>Email: marcuspellow22@mailbox.com</p>
      <p>Mobile phone: 0400 512 873</p>
      <p>RBCA Licence number: 4830915</p>
    </div>

    <div class="scene" role="img" aria-label="Photo of a two-storey brick house with a green lawn, with a cartoon carpenter in a blue hard hat and overalls giving a thumbs up while holding a blueprint sheet"></div>

    <ul class="services">
      <li>decks/decking</li>
      <li>external stairs &amp; railings</li>
      <li>install windows &amp; doors</li>
      <li>roofs &amp; gutters</li>
      <li>small additions</li>
      <li>built-in wardrobes</li>
      <li>finish work</li>
      <li>demolition</li>
    </ul>
  </main>
</body>
</html>
```